Northbrook Vertebral Clinic of Weldon
Spine Surgeon
Professional
Grant Pellow, DO
Board Certified, Fellowship Trained, Reconstructive and Minimally Invasive Spine Surgery
5183 W. Tamsworth Rd., Suite 204
Weldon, TX 75820
unknown at this time
unknown
grantjpellow@mailvex.net
www.NorthbrookVertebralClinic.net
Board Certified, Orthopedic surgery
Fellowship Trained, Reconstructive and Minimally Invasive Spine Surgery
Clearly highlight that I am board certified and fellowship trained in spine surgery.
I am setting up a new office and do not have phone lines ect. I will be changing my email address to a business account
Treatment of:
Back and Neck Pain,
Arm and Leg Pain,
Degenerative Disc Disease of the Spine,
Spinal Stenosis,
Herniated Discs,
Scoliosis and Spinal Deformities,
Spinal Tumors and Infections,
Spinal Compression Fractures,
Worker's Compensation Injuries,
Motor Vehicle Injuries

```html
<!DOCTYPE html>
<html lang="en">
<head>
<meta charset="utf-8">
<title>Northbrook Vertebral Clinic of Weldon — Stationery</title>
<link href="https://fonts.googleapis.com/css2?family=EB+Garamond:ital,wght@0,400;0,600;1,400;1,600&display=swap" rel="stylesheet">
<style>
  :root {
    --navy: #1f2f5c;
    --navy-deep: #16234a;
    --paper: #ffffff;
    --ink: #2b3550;
    --mist: #e3e7ef;
    --steel: #aab4c7;
    --steel-dark: #97a3b9;
    --flap: #c9d0de;
    --window: #f6f7fa;
    --window-edge: #c7cdd9;
    --ground: #d9dee8;
  }
  * { margin: 0; padding: 0; box-sizing: border-box; }
  html, body { width: 1200px; height: 737px; overflow: hidden; }
  body {
    background: var(--ground);
    font-family: "EB Garamond", Georgia, serif;
    color: var(--ink);
    position: relative;
  }
  .sheet { position: absolute; background: var(--paper); overflow: hidden; box-shadow: 0 2px 8px rgba(20,30,60,.25); }

  .wordmark { display: flex; align-items: center; gap: 8px; color: var(--navy); }
  .wordmark__dot { width: 20px; height: 20px; border-radius: 50%; background: var(--navy); flex: none; }
  .wordmark__name { font-weight: 600; text-transform: uppercase; letter-spacing: .04em; line-height: 1.05; }

  .band { position: absolute; left: 0; right: 0; bottom: 0; background: var(--navy); color: #fff; font-weight: 600; white-space: nowrap; }
  .faint-disc { position: absolute; border-radius: 50%; background: var(--mist); }

  dl.contact-list { display: grid; grid-template-columns: 34px auto; }
  dl.contact-list dt::after { content: ":"; float: right; padding-right: 6px; }

  /* letterhead */
  .letterhead { z-index: 1; left: 629px; top: 29px; width: 435px; height: 607px; }
  .letterhead .wordmark { position: absolute; left: 30px; top: 38px; width: 160px; }
  .letterhead .wordmark__name { font-size: 12px; }
  .letterhead .contact { position: absolute; left: 200px; top: 36px; font-size: 9px; line-height: 1.45; }
  .letterhead .faint-disc { width: 150px; height: 150px; right: -30px; bottom: 10px; }
  .letterhead .band { height: 20px; font-size: 9.5px; padding: 4px 24px; }

  /* envelope */
  .envelope { z-index: 2; left: 36px; top: 318px; width: 727px; height: 330px; }
  .envelope__flap { position: absolute; left: 0; top: 0; width: 727px; height: 120px; }
  .envelope .wordmark { position: absolute; left: 32px; top: 78px; width: 200px; }
  .envelope .wordmark__name { font-size: 14px; }
  .envelope__window { position: absolute; left: 118px; top: 160px; width: 290px; height: 80px; border: 1px solid var(--window-edge); border-radius: 6px; background: var(--window); }
  .envelope__return { position: absolute; left: 32px; top: 280px; font-size: 9.5px; }
  .envelope .band { height: 20px; font-size: 10px; padding: 4px 32px; }

  /* business card front */
  .card-front { z-index: 3; left: 713px; top: 228px; width: 408px; height: 252px; }
  .card-front .person { position: absolute; left: 22px; top: 20px; width: 180px; }
  .card-front .person__name { font-size: 12.5px; font-weight: 600; color: var(--navy); text-transform: uppercase; letter-spacing: .02em; }
  .card-front .person__creds { font-size: 8.5px; line-height: 1.35; margin-top: 10px; }
  .card-front .contact { position: absolute; left: 211px; top: 20px; font-size: 8.5px; line-height: 1.45; }
  .card-front .wordmark { position: absolute; left: 100px; top: 152px; width: 200px; }
  .card-front .wordmark__name { font-size: 13px; }
  .card-front .faint-disc { width: 150px; height: 150px; right: -40px; bottom: -30px; }
  .card-front .band { height: 24px; font-size: 10px; padding: 5px 22px; }

  /* business card back */
  .card-back { z-index: 3; left: 713px; top: 533px; width: 408px; height: 187px; background: var(--steel); }
  .card-back .faint-disc { width: 140px; height: 140px; left: -40px; top: -30px; background: var(--steel-dark); opacity: .5; }
  .card-back__title { position: absolute; left: 120px; top: 12px; font-size: 19px; font-style: italic; color: var(--navy-deep); font-weight: 600; }
  .card-back__list { position: absolute; left: 120px; top: 42px; list-style: none; font-size: 9px; line-height: 1.38; color: var(--navy-deep); }
</style>
</head>
<body>

  <section class="sheet letterhead" aria-label="Letterhead, A4 size">
    <div class="wordmark">
      <span class="wordmark__dot"></span>
      <span class="wordmark__name">Northbrook Vertebral Clinic of Weldon</span>
    </div>
    <div class="contact">
      <p>5183 W. Tamsworth Rd., Suite 204</p>
      <p>Weldon, TX 75820</p>
      <dl class="contact-list">
        <dt>Phone</dt><dd>unknown</dd>
        <dt>Cell</dt><dd>unknown</dd>
        <dt>Fax</dt><dd>unknown</dd>
        <dt>Email</dt><dd>grantjpellow@mailvex.net</dd>
      </dl>
    </div>
    <div class="faint-disc"></div>
    <div class="band">www.NorthbrookVertebralClinic.net</div>
  </section>

  <section class="sheet envelope" aria-label="Envelope, number 10 size">
    <svg class="envelope__flap" viewBox="0 0 727 120" preserveAspectRatio="none" aria-hidden="true">
      <path d="M0 0 H727 V30 C620 30 510 62 395 104 C360 116 345 116 322 104 C225 62 110 30 0 30 Z" fill="#c9d0de"/>
    </svg>
    <div class="wordmark">
      <span class="wordmark__dot"></span>
      <span class="wordmark__name">Northbrook Vertebral Clinic of Weldon</span>
    </div>
    <div class="envelope__window"></div>
    <p class="envelope__return">5183 W. Tamsworth Rd., Suite 204 &nbsp;&bull;&nbsp; Weldon, TX 75820</p>
    <div class="band">www.NorthbrookVertebralClinic.net</div>
  </section>

  <section class="sheet card-front" aria-label="Business card front">
    <div class="person">
      <h1 class="person__name">Grant Pellow, DO</h1>
      <p class="person__creds">Board Certified<br>Fellowship Trained<br>Reconstructive and<br>Minimally Invasive Spine Surgery</p>
    </div>
    <div class="contact">
      <p>5183 W. Tamsworth Rd., Suite 204</p>
      <p>Weldon, TX 75820</p>
      <dl class="contact-list">
        <dt>Tel</dt><dd>unknown</dd>
        <dt>Cell</dt><dd>unknown</dd>
        <dt>Fax</dt><dd>unknown</dd>
        <dt>Email</dt><dd>grantjpellow@mailvex.net</dd>
      </dl>
    </div>
    <div class="faint-disc"></div>
    <div class="wordmark">
      <span class="wordmark__dot"></span>
      <span class="wordmark__name">Northbrook Vertebral Clinic of Weldon</span>
    </div>
    <div class="band">www.NorthbrookVertebralClinic.net</div>
  </section>

  <section class="sheet card-back" aria-label="Business card back">
    <div class="faint-disc"></div>
    <h2 class="card-back__title">Treatment of:</h2>
    <ul class="card-back__list">
      <li>Back and Neck Pain,</li>
      <li>Arm and Leg Pain,</li>
      <li>Degenerative Disc Disease of the Spine,</li>
      <li>Spinal Stenosis,</li>
      <li>Herniated Discs,</li>
      <li>Scoliosis and Spinal Deformities,</li>
      <li>Spinal Tumors and Infections,</li>
      <li>Spinal Compression Fractures,</li>
      <li>Worker's Compensation Injuries,</li>
      <li>Motor Vehicle Injuries</li>
    </ul>
  </section>

</body>
</html>
```